Free Offer Book Cover

I am creating a funnel page where I offer a free download of a PDF called. Twelve-Week Launch Kit. A road map for new leaders. I have included samples of other book covers. It can look like a book, or a checklist, or something that illustrates what they are getting. Bright Harbor Coaching is the company if you could get the logo into the book cover as well.

Target Market(s)

New leaders, young professionals

Font styles to use
Sans Serif

Requirements
Must have
• Name of content. Twelve-Week Launch Kit for new leaders.

```html
<!DOCTYPE html>
<html lang="en">
<head>
<meta charset="utf-8">
<title>Bright Harbor Coaching – Twelve-Week Launch Kit</title>
<link rel="stylesheet" href="https://fonts.googleapis.com/css2?family=Nunito:wght@400;600&family=Roboto+Condensed:wght@300;400&family=Oswald:wght@400;500;700&family=Open+Sans:wght@400;700&display=swap">
<style>
  :root {
    --page-bg: #2e2e2e;
    --accent: #e23b2e;
    --accent-text: #e4473b;
    --cover-red: #ee3a47;
    --white: #ffffff;
    --field-bg: #f1f1f1;
    --field-text: #6f6f6f;
    --tag-bg: #4a4a4a;
    --cover-dark: #141414;
    --cover-mid: #3a3a3a;
    --spine: #0c0c0c;
  }
  html, body {
    margin: 0;
    padding: 0;
    width: 1200px;
    height: 754px;
    overflow: hidden;
    background: var(--page-bg);
  }
  .page {
    position: relative;
    width: 1200px;
    height: 754px;
    background: var(--page-bg);
    font-family: "Nunito", sans-serif;
  }
  .offer-panel {
    position: absolute;
    left: 21px;
    top: 19px;
    width: 550px;
    height: 710px;
    background: var(--white);
    border: 2px solid var(--accent);
    overflow: hidden;
  }
  .book {
    position: absolute;
    left: 76px;
    top: 195px;
    width: 300px;
    height: 430px;
    transform-origin: 0 0;
    transform: matrix(0.87, -0.187, 0.337, 0.96, 0, 0);
  }
  .book-spine {
    position: absolute;
    left: -16px;
    top: 4px;
    width: 16px;
    height: 430px;
    background: var(--spine);
    border-radius: 3px 0 0 3px;
    overflow: hidden;
  }
  .book-spine span {
    position: absolute;
    left: 4px;
    top: 12px;
    writing-mode: vertical-rl;
    font-family: "Oswald", sans-serif;
    font-weight: 500;
    font-size: 9px;
    letter-spacing: .5px;
    color: #cfcfcf;
    white-space: nowrap;
  }
  .book-cover {
    position: absolute;
    inset: 0;
    background: linear-gradient(135deg, var(--cover-mid) 0%, #222 45%, var(--cover-dark) 100%);
    border-radius: 0 3px 3px 0;
    box-shadow: 4px 6px 10px rgba(0,0,0,.35);
    font-family: "Oswald", sans-serif;
    text-align: center;
  }
  .cover-kicker {
    position: absolute;
    top: 22px;
    left: 0;
    right: 0;
    display: flex;
    align-items: center;
    justify-content: center;
    gap: 10px;
    font-weight: 700;
    font-size: 30px;
    color: var(--cover-red);
    line-height: 1;
  }
  .cover-kicker::before, .cover-kicker::after {
    content: "";
    width: 34px;
    height: 5px;
    background: var(--cover-red);
  }
  .cover-title {
    position: absolute;
    top: 62px;
    left: 0;
    right: 0;
    font-weight: 700;
    font-size: 104px;
    line-height: 1;
    color: var(--cover-red);
    letter-spacing: 1px;
  }
  .cover-subtitle {
    position: absolute;
    top: 186px;
    left: 0;
    right: 0;
    font-weight: 700;
    font-size: 46px;
    line-height: 1;
    color: #eeeeee;
  }
  .cover-brand {
    position: absolute;
    top: 262px;
    left: 0;
    right: 0;
    font-family: "Nunito", sans-serif;
    font-weight: 600;
    font-size: 17px;
    color: var(--cover-red);
  }
  .cover-rule {
    position: absolute;
    top: 348px;
    left: 30px;
    right: 30px;
    height: 6px;
    background: var(--cover-red);
  }
  .cover-tagline {
    position: absolute;
    top: 366px;
    left: 0;
    right: 0;
    font-weight: 500;
    font-size: 20px;
    letter-spacing: .5px;
    color: var(--cover-red);
  }
  .brand {
    position: absolute;
    left: 615px;
    width: 553px;
    top: 62px;
    display: flex;
    justify-content: center;
    align-items: center;
    gap: 12px;
  }
  .brand-mark {
    width: 22px;
    height: 22px;
    background: var(--accent);
  }
  .brand-name {
    font-family: "Nunito", sans-serif;
    font-weight: 600;
    font-size: 34px;
    color: var(--accent);
    letter-spacing: 1px;
  }
  .headline {
    position: absolute;
    left: 600px;
    width: 583px;
    top: 192px;
    margin: 0;
    text-align: center;
    font-weight: 400;
    font-size: 74px;
    line-height: 1;
    color: var(--accent);
  }
  .subhead {
    position: absolute;
    left: 600px;
    width: 583px;
    top: 272px;
    margin: 0;
    text-align: center;
    font-weight: 400;
    font-size: 35px;
    line-height: 38px;
    color: var(--white);
  }
  .offer-lines {
    position: absolute;
    left: 600px;
    width: 583px;
    top: 354px;
    margin: 0;
    text-align: center;
    font-family: "Roboto Condensed", sans-serif;
    font-weight: 300;
    font-size: 27px;
    line-height: 40px;
    color: var(--accent-text);
  }
  .signup-form { margin: 0; }
  .field {
    position: absolute;
    left: 615px;
    width: 553px;
    height: 51px;
    background: var(--field-bg);
    border-radius: 3px;
    box-shadow: 0 2px 3px rgba(0,0,0,.35);
  }
  .field-name { top: 468px; }
  .field-email { top: 542px; }
  .field-placeholder {
    position: absolute;
    left: 20px;
    top: 15px;
    font-family: "Open Sans", sans-serif;
    font-size: 15px;
    color: var(--field-text);
  }
  .field-tag {
    position: absolute;
    left: 11px;
    bottom: -6px;
    padding: 1px 4px;
    background: var(--tag-bg);
    color: #ddd;
    font-family: "Open Sans", sans-serif;
    font-weight: 700;
    font-size: 7px;
    letter-spacing: .3px;
  }
  .submit-button {
    position: absolute;
    left: 615px;
    top: 626px;
    width: 553px;
    height: 82px;
    background: var(--accent);
    border-radius: 3px;
    box-shadow: 0 2px 4px rgba(0,0,0,.4);
    display: flex;
    align-items: center;
    justify-content: center;
    font-family: "Oswald", sans-serif;
    font-size: 39px;
    color: var(--white);
  }
  .submit-button .field-tag { bottom: -5px; left: 12px; }
</style>
</head>
<body>
<main class="page">
  <section class="offer-panel">
    <div class="book">
      <div class="book-spine"><span>TWELVE-WEEK LAUNCH KIT – A ROAD MAP FOR NEW LEADERS</span></div>
      <div class="book-cover">
        <div class="cover-kicker">TWELVE</div>
        <div class="cover-title">WEEK</div>
        <div class="cover-subtitle">LAUNCH KIT</div>
        <div class="cover-brand">Bright Harbor Coaching</div>
        <div class="cover-rule"></div>
        <div class="cover-tagline">A ROAD MAP FOR NEW LEADERS</div>
      </div>
    </div>
  </section>

  <div class="brand">
    <span class="brand-mark"></span>
    <span class="brand-name">Bright Harbor Coaching</span>
  </div>

  <h1 class="headline">DISCOVER</h1>
  <p class="subhead">What you need to do NOW to<br>become a Bright Harbor Leader!</p>
  <p class="offer-lines">Get your free Twelve-Week Launch Kit.<br>The Road Map for New Leaders.</p>

  <form class="signup-form">
    <div class="field field-name">
      <span class="field-placeholder">Enter Your Name Here...</span>
      <span class="field-tag">NAME</span>
    </div>
    <div class="field field-email">
      <span class="field-placeholder">Enter Your Email Address Here...</span>
      <span class="field-tag">EMAIL</span>
    </div>
    <div class="submit-button">
      Click to Get Your Launch Kit
      <span class="field-tag">SUBMITS THE PAGE</span>
    </div>
  </form>
</main>
</body>
</html>
```